Business Card Design For Financial Company

Create a new design for company's business card. The corporate logo is attached in several formats. Our new website design is also attached and we would like the business cards to reflect this.
Card needs to contain the following info:
Name
Job Title
Legal company name - eg Varomel Holdings (Asia) Ltd
Address - eg 517-09 Brellford Plaza,46 Tamsworth Lane, Hong Kong
Direct tel
Main tel
Fax
Email
Website URL
MS word format preferred. Other formats that can be edited on standard PC also OK.
Updates
Please note the the "VAROMEL" logo nameĀ font is "Gill Sans MT" on Windows
Target Market(s)
Instituation Investors
Industry/Entity Type
Business
Look and feel
Each slider illustrates characteristics of the customer's brand and the style your logo design should communicate.

```html
<!DOCTYPE html>
<html lang="en">
<head>
<meta charset="utf-8">
<title>Varomel Holdings – Business Card</title>
<link rel="stylesheet" href="https://fonts.googleapis.com/css2?family=Open+Sans:ital,wght@0,400;0,600;1,400&family=Tinos&display=swap">
<style>
  :root {
    --card-white: #ffffff;
    --card-blush: #f7e4e4;
    --mark-neutral: #e4e1e1;
    --ink-strong: #505050;
    --ink-body: #3a3a3a;
    --ink-muted: #9a9a9a;
    --rule: #7a7a7a;
  }
  html, body {
    margin: 0;
    padding: 0;
    width: 1200px;
    height: 685px;
    overflow: hidden;
    background: var(--card-white);
  }
  .card {
    position: relative;
    width: 1200px;
    height: 685px;
    overflow: hidden;
    font-family: "Open Sans", Arial, sans-serif;
    background:
      radial-gradient(ellipse 520px 460px at 1080px 600px, var(--card-blush) 0%, rgba(247,228,228,0) 100%),
      linear-gradient(90deg, var(--card-white) 0%, #fdf4f4 55%, #faeaea 100%);
  }
  .brand-mark {
    position: absolute;
    left: 180px;
    top: 127px;
    width: 120px;
    height: 120px;
    background: var(--mark-neutral);
  }
  .brand-name {
    position: absolute;
    left: 0;
    width: 480px;
    top: 330px;
    margin: 0;
    text-align: center;
    font-weight: 400;
    font-size: 64px;
    letter-spacing: 2px;
    color: var(--ink-strong);
  }
  .brand-legal {
    position: absolute;
    left: 0;
    width: 480px;
    top: 456px;
    margin: 0;
    text-align: center;
    font-size: 26px;
    color: var(--ink-strong);
  }
  .divider {
    position: absolute;
    left: 527px;
    top: 53px;
    width: 2px;
    height: 576px;
    background: var(--rule);
  }
  .person-name {
    position: absolute;
    left: 568px;
    top: 56px;
    margin: 0;
    font-weight: 400;
    font-size: 37px;
    letter-spacing: 1px;
    color: var(--ink-strong);
  }
  .person-title {
    position: absolute;
    left: 570px;
    top: 122px;
    margin: 0;
    font-size: 28px;
    letter-spacing: 1px;
    color: var(--ink-muted);
  }
  .address {
    position: absolute;
    left: 573px;
    top: 224px;
    margin: 0;
    font-style: italic;
    font-size: 27px;
    line-height: 37px;
    color: var(--ink-body);
  }
  .phones {
    position: absolute;
    left: 747px;
    top: 350px;
    margin: 0;
    font-family: "Tinos", "Times New Roman", serif;
    font-size: 30px;
    line-height: 44px;
    color: var(--ink-body);
  }
  .web {
    position: absolute;
    left: 747px;
    top: 529px;
    margin: 0;
    font-size: 27px;
    line-height: 45px;
    color: var(--ink-body);
  }
</style>
</head>
<body>
  <main class="card">
    <div class="brand-mark" aria-hidden="true"></div>
    <h1 class="brand-name">VAROMEL</h1>
    <p class="brand-legal">Holdings (Asia) Ltd</p>

    <div class="divider"></div>

    <h2 class="person-name">DORIAN PELLAMY</h2>
    <p class="person-title">STAFF</p>

    <p class="address">517-09 Brellford Plaza,<br>46 Tamsworth Lane, Hong Kong</p>

    <p class="phones">
      direct + (312) 555-0184<br>
      main + (312) 555-0185<br>
      fax + (312) 555-0185
    </p>

    <p class="web">
      dorian.varomelholdings.com<br>
      www.varomelholdings.com
    </p>
  </main>
</body>
</html>
```